LANTERNHILL Pizza and Wraps

We need a website for a new restaurant called LANTERNHILL "PIZZA AND WRAPS".
I have attached fonts, background images, logo, images, content etc.
can provide you with what you need to get the website design done fast and easy
Updates

I have uploaded more images of the venue and some menu items. let me know if there is anything I need to provide to make your mission clear and easy

Reason: i would like a little time to provide more feedback to designers

Industry/Entity Type

Restaurant

Coding

Coded - Design and coding required

Number of Pages Required

5+ page

Colors

Designer to choose colors to be used in the design.

Requirements
Must have
• PAGES:
• Our Story
• Menu
• Reservations
• Catering & Delivery
• Contact

```html
<!DOCTYPE html>
<html lang="en">
<head>
<meta charset="utf-8">
<title>Lanternhill Pizza and Wraps</title>
<link rel="stylesheet" href="https://fonts.googleapis.com/css2?family=Raleway:wght@300;400;600;700;800&family=Kaushan+Script&display=swap">
<style>
:root{
  --red:#e21f2b;
  --ink:#2b2b2b;
  --muted:#8a8a8a;
  --dark:#1c1714;
  --darker:#120f0d;
  --panel:#2c2724;
  --white:#ffffff;
  --line:#d9d9d9;
}
*{box-sizing:border-box;margin:0;padding:0}
html,body{width:1200px;height:4369px;overflow:hidden}
body{font-family:"Raleway",sans-serif;color:var(--ink);background:var(--white);position:relative}
section,header,footer{position:relative;width:1200px;overflow:hidden}
.abs{position:absolute}
.center{left:0;width:1200px;text-align:center}
.wide-title{font-family:"Raleway",sans-serif;font-weight:300;letter-spacing:10px;text-transform:uppercase;color:var(--white);font-size:44px}
.btn-red{position:absolute;background:var(--red);color:var(--white);font-weight:700;font-size:12px;letter-spacing:1px;text-transform:uppercase;display:flex;align-items:center;justify-content:center}

/* hero */
.hero{height:597px;background:radial-gradient(ellipse at 35% 55%,#3d3a1f 0%,#262114 40%,#140f0b 80%)}
.brand{font-family:"Raleway",sans-serif;font-weight:800;color:var(--red);font-size:26px;letter-spacing:1px}
.nav{left:685px;top:28px;display:flex;gap:28px;font-size:11px;font-weight:700;color:var(--white);letter-spacing:.5px}
.nav .active{border-bottom:2px solid var(--red);padding-bottom:6px}
.dropdown{left:920px;top:60px;width:90px;background:#000;padding:8px 10px;font-size:10px;font-weight:700;color:var(--white);line-height:20px}
.hero-title{font-family:"Kaushan Script",cursive;color:var(--white);font-size:58px;line-height:60px}
.hero-info{font-size:12px;color:var(--white);display:flex;justify-content:center;gap:8px;align-items:center}
.hero-text{left:390px;width:420px;top:344px;text-align:center;color:#e6e6e6;font-size:13px;line-height:20px}

/* story */
.story{height:335px}
.story-title{left:122px;top:60px;font-size:20px;letter-spacing:5px;font-weight:400;color:var(--ink);text-transform:uppercase}
.story-title::after{content:"";display:block;width:34px;height:2px;background:var(--red);margin-top:6px}
.story-text{left:122px;top:118px;width:475px;font-size:11px;line-height:17px;color:var(--muted)}
.video{left:647px;top:50px;width:431px;height:236px;background:linear-gradient(160deg,#3a2a1f,#1b1410 70%)}

/* banners */
.banner{height:184px;background:linear-gradient(90deg,#3b2117 0%,#5a3a2a 30%,#2a1c16 60%,#6b3d2b 100%)}
.banner-shade{inset:0;background:rgba(0,0,0,.35)}

/* menu */
.menu{height:763px}
.menu-intro{left:198px;width:807px;text-align:center;color:var(--muted);font-size:14px;line-height:22px}
.tabs{left:330px;width:540px;top:262px;display:flex;justify-content:center;gap:34px;font-size:11px;font-weight:700;color:#555;border-bottom:1px solid var(--line);padding-bottom:9px}
.tabs .on{color:var(--ink);border-bottom:2px solid var(--red);padding-bottom:7px;margin-bottom:-11px}
.menu-col{top:340px;width:393px}
.item{height:66px}
.item-head{display:flex;font-size:13px;font-weight:700;color:#222;align-items:baseline}
.item-head .dots{flex:1;border-bottom:1px dotted #999;margin:0 4px}
.item-desc{font-size:10px;line-height:14px;color:var(--muted);margin-top:3px}

/* gallery */
.gallery{height:909px}
.photo{position:absolute}

/* events */
.events{height:699px;background:linear-gradient(180deg,#181412,#231d1a 50%,#161210)}
.ev-sub{font-size:18px;color:var(--white);letter-spacing:1px}
.ev-lead{font-size:14px;font-weight:700;color:var(--white)}
.ev-text{left:233px;width:743px;text-align:center;color:#cfcfcf;font-size:13px;line-height:20px}
.btn-ghost{position:absolute;border:1px solid #bbb;color:var(--white);font-size:10px;font-weight:700;letter-spacing:.5px;display:flex;align-items:center;justify-content:center;text-transform:uppercase}
.card{top:423px;width:455px;height:204px;background:rgba(70,62,56,.75);padding:26px 26px}
.card h3{font-size:13px;font-weight:700;color:var(--white);letter-spacing:.5px}
.card p{font-size:10.5px;line-height:16px;color:#cfcfcf;margin-top:10px;width:330px;text-transform:uppercase}

/* reserve */
.reserve{height:379px;background:var(--dark)}
.res-line{font-size:13px;color:var(--white)}
.field-label{font-size:10px;color:var(--white);font-weight:600}
.field{height:35px;border:1px solid #888;background:var(--white)}

/* footer */
.footer{height:320px;background:var(--darker);color:var(--white)}
.foot-head{font-size:15px;letter-spacing:4px;color:var(--red);font-weight:400;text-transform:uppercase}
.foot-text{font-size:11px;line-height:17px;color:#ddd}
.foot-input{left:752px;width:291px;background:#000;border:1px solid #333;font-size:10px;color:#ccc;padding:10px}
.copy{font-size:10px;color:#999}
</style>
</head>
<body>

<header class="hero">
  <div class="abs brand" style="left:122px;top:15px">LANTERNHILL</div>
  <nav class="abs nav">
    <span class="active">HOME</span><span>OUR STORY</span><span>MENU</span><span>GALLERY</span><span class="active">EVENTS</span><span>CONTACT</span>
  </nav>
  <svg class="abs" style="left:1062px;top:26px" width="16" height="16" viewBox="0 0 16 16"><circle cx="6.5" cy="6.5" r="5" fill="none" stroke="#fff" stroke-width="2"/><line x1="10" y1="10" x2="15" y2="15" stroke="#fff" stroke-width="2"/></svg>
  <div class="abs dropdown">DELIVERY<br>CATERING</div>

  <div class="abs center hero-title" style="top:95px">Lanternhill<br>pizza &amp; wraps</div>
  <div class="abs center hero-info" style="top:240px">
    <svg width="10" height="13" viewBox="0 0 10 13"><path d="M5 0a5 5 0 0 1 5 5c0 4-5 8-5 8S0 9 0 5a5 5 0 0 1 5-5z" fill="#fff"/><circle cx="5" cy="5" r="1.8" fill="#222"/></svg>
    <span>212 Orchard Lane, Millbrook MB4 7QT</span>
  </div>
  <div class="abs center hero-info" style="top:264px">
    <svg width="12" height="12" viewBox="0 0 12 12"><circle cx="6" cy="6" r="5" fill="none" stroke="#fff" stroke-width="1.5"/><path d="M6 3v3h2.5" stroke="#fff" stroke-width="1.5" fill="none"/></svg>
    <span>10:00 am – 11:00 pm</span>
    <svg width="12" height="12" viewBox="0 0 12 12" style="margin-left:10px"><path d="M2 1l2.5 0 1 3-1.5 1a7 7 0 0 0 3 3l1-1.5 3 1V11C6 11 1 6 1 2z" fill="#fff"/></svg>
    <span>800 555 0142</span>
  </div>
  <p class="abs hero-text">We introduce new cultures to visitors through cuisines of various countries offering a special dish for everyone regardless of their food preferences</p>
  <div class="btn-red" style="left:510px;top:428px;width:180px;height:44px">Make a reservation</div>
</header>

<section class="story">
  <h2 class="abs story-title">Our Story</h2>
  <p class="abs story-text">Rich in heritage, Lanternhill is a gathering place celebrating the Mediterranean's finest. Lanternhill is the ultimate escape – the perfect spot to enjoy sensational food and drinks that showcases everything the Mediterranean has to offer in a single, sophisticated setting. Arrive on early morning walk to the bakery around the corner is a way of life: nothing beats the first batch of bread from the oven to start your day. So we combined a variety of best ingredients and flatbreads for you to enjoy that experience wherever you get the urge to do so.</p>
  <div class="abs video" role="img" aria-label="Video thumbnail of the restaurant review showing the dining room">
    <div class="abs" style="left:0;top:0;width:431px;height:34px;background:rgba(0,0,0,.55)"></div>
    <div class="abs" style="left:12px;top:10px;font-size:12px;font-weight:700;color:#fff">Restaurant Review - Lanternhill pizza &amp; wraps</div>
    <svg class="abs" style="left:400px;top:9px" width="16" height="14" viewBox="0 0 16 14"><path d="M10 0l6 6-6 6V8C5 8 2 9 0 13 1 7 4 4 10 4z" fill="#fff"/></svg>
    <div class="abs" style="left:0;top:210px;width:431px;height:26px;background:rgba(0,0,0,.7)"></div>
    <svg class="abs" style="left:10px;top:217px" width="10" height="12" viewBox="0 0 10 12"><path d="M0 0l10 6-10 6z" fill="#fff"/></svg>
    <div class="abs" style="left:30px;top:222px;width:340px;height:3px;background:#666"></div>
    <div class="abs" style="left:30px;top:222px;width:110px;height:3px;background:var(--red)"></div>
    <div class="abs" style="left:385px;top:217px;font-size:9px;color:#fff">05:48</div>
  </div>
</section>

<section class="banner" role="img" aria-label="Photo of the brick-walled restaurant entrance">
  <div class="abs banner-shade"></div>
  <h2 class="abs center wide-title" style="top:35px">Our Menu</h2>
  <div class="abs center" style="top:102px;color:#fff;font-size:16px;letter-spacing:3px">PIZZAS &nbsp;|&nbsp; WRAPS &nbsp;|&nbsp; DESSERTS &nbsp;|&nbsp; BEVERAGES</div>
</section>

<section class="menu">
  <p class="abs menu-intro" style="top:44px">Quality food is devotion to seasonal, finest ingredients, and meticulous care in bringing it to life on the plate. At Lanternhill, the emphasis is on an experience that extends from a great menu to a relaxed, warm environment of the venue. Choose from our delicious, made from scratch and hand-rolled selection of Pizza and Wraps, where our Chefs stand ready to bake it for you on order and straight from our traditional oven to your plate.</p>
  <p class="abs menu-intro" style="top:156px">Lanternhill promises an unrivalled drinking and dining experience. Our Mediterranean focus is further complemented by a considered variety of beverages and desserts to satisfy your choice of flavours.<br>Discover Mediterranean tastes &amp; crafted beverages</p>
  <div class="abs tabs"><span class="on">ALL</span><span>PIZZAS</span><span>WRAPS</span><span>DESSERTS</span><span>BEVERAGES</span></div>

  <div class="abs menu-col" style="left:169px">
    <div class="item"><div class="item-head">LANTERNHILL SPECIAL PIZZA<span class="dots"></span>$22.00</div><div class="item-desc">( Two eggs cooked to order with grits, sawmill gravy, homemade buttermilk biscuits &amp; real butter )</div></div>
    <div class="item"><div class="item-head">LANTERNHILL SPECIAL PIZZA<span class="dots"></span>$22.00</div><div class="item-desc">( Start your day with a mix of low fat vanilla yogurt, fresh seasonal fruit topped with our honey mix )</div></div>
    <div class="item"><div class="item-head">LANTERNHILL SPECIAL PIZZA<span class="dots"></span>$22.00</div><div class="item-desc">( Three eggs cooked to order with a full order of bacon and sausage patties )</div></div>
    <div class="item"><div class="item-head">LANTERNHILL SPECIAL PIZZA<span class="dots"></span>$22.00</div><div class="item-desc">( Fresh wheatberries oats, crunchy fennel, smashed avocado, yoghurt &amp; chilli )</div></div>
    <div class="item"><div class="item-head">LANTERNHILL SPECIAL PIZZA<span class="dots"></span>$29.00</div><div class="item-desc">( Stuffed with prosciutto &amp; provolone, breadcrumbed &amp; topped with a free-range egg &amp; black summer truffle )</div></div>
  </div>
  <div class="abs menu-col" style="left:635px">
    <div class="item"><div class="item-head">LANTERNHILL SPECIAL PIZZA<span class="dots"></span>$22.00</div><div class="item-desc">( Two eggs cooked to order with grits, sawmill gravy, homemade buttermilk biscuits &amp; real butter )</div></div>
    <div class="item"><div class="item-head">LANTERNHILL SPECIAL PIZZA<span class="dots"></span>$22.00</div><div class="item-desc">( Start your day with a mix of low fat vanilla yogurt, fresh seasonal fruit topped with our honey mix )</div></div>
    <div class="item"><div class="item-head">LANTERNHILL SPECIAL PIZZA<span class="dots"></span>$22.00</div><div class="item-desc">( Three eggs cooked to order with a full order of bacon and sausage patties )</div></div>
    <div class="item"><div class="item-head">LANTERNHILL SPECIAL PIZZA<span class="dots"></span>$22.00</div><div class="item-desc">( Fresh wheatberries oats, crunchy fennel, smashed avocado, yoghurt &amp; chilli )</div></div>
    <div class="item"><div class="item-head">LANTERNHILL SPECIAL PIZZA<span class="dots"></span>$22.00</div><div class="item-desc">( Stuffed with prosciutto &amp; provolone, breadcrumbed &amp; topped with a free-range egg &amp; black summer truffle )</div></div>
  </div>
</section>

<section class="banner" role="img" aria-label="Photo of the restaurant brick facade at night">
  <div class="abs banner-shade"></div>
  <h2 class="abs center wide-title" style="top:30px">Our Gallery</h2>
  <div class="abs center" style="top:104px;color:#fff;font-size:16px;letter-spacing:1px">CHECK OUT OUR SPACE AND FOODS</div>
</section>

<section class="gallery">
  <div class="photo" style="left:122px;top:58px;width:222px;height:138px;background:linear-gradient(135deg,#9a5a3c,#c9a27f)" role="img" aria-label="Brick wall corner with plants"></div>
  <div class="photo" style="left:355px;top:58px;width:228px;height:138px;background:linear-gradient(135deg,#6b5a3d,#c7b48a)" role="img" aria-label="Plated food on a table"></div>
  <div class="photo" style="left:122px;top:206px;width:461px;height:292px;background:radial-gradient(circle at 45% 50%,#e6c46a,#d7c59f 45%,#e9e2d4 75%)" role="img" aria-label="Bowl of hummus with olive oil and chickpeas"></div>
  <div class="photo" style="left:594px;top:58px;width:484px;height:440px;background:radial-gradient(ellipse at 50% 15%,#f1c568,#8a5a35 45%,#3e2a1e 90%)" role="img" aria-label="Restaurant interior with lit ceiling and windows"></div>
  <div class="photo" style="left:122px;top:510px;width:542px;height:312px;background:linear-gradient(135deg,#3b3b3b,#8d8d8d 50%,#2a2a2a)" role="img" aria-label="Black and white view of the dining tables"></div>
  <div class="photo" style="left:682px;top:510px;width:215px;height:312px;background:linear-gradient(160deg,#5b4a3a,#a06a4a 60%,#3a2a22)" role="img" aria-label="Counter area with tiled floor and plants"></div>
  <div class="photo" style="left:909px;top:510px;width:169px;height:152px;background:radial-gradient(circle,#c0392b,#6d9a3a 55%,#e8e4dc 85%)" role="img" aria-label="Fresh salad plate"></div>
  <div class="photo" style="left:909px;top:670px;width:169px;height:152px;background:linear-gradient(135deg,#e8c88a,#f5e6c4 60%,#d9b27a)" role="img" aria-label="Grilled wraps"></div>
</section>

<section class="events" role="img" aria-label="Dimmed photo of the venue interior">
  <h2 class="abs center wide-title" style="top:40px">About Events</h2>
  <div class="abs center ev-sub" style="top:98px">JOIN US FOR SOMETHING SPECIAL</div>
  <div class="abs center ev-lead" style="top:166px">A special event requires a unique experience. Lanternhill comes to You!</div>
  <p class="abs ev-text" style="top:210px">The quality of our cuisine directly in your home with Passion and professionality in the planning of the menu.Order a single portion and receive it in the comfort of your home or call us for parties, anniversaries and other events. Let Lanternhill cater for your next event and make it unforgettable. Create your own unique environment and atmosphere to enjoy our selection of premium quality food and beverages.</p>
  <div class="btn-ghost" style="left:480px;top:320px;width:240px;height:30px">Enquire about hosting a function</div>

  <div class="abs card" style="left:122px">
    <h3>DELIVERY</h3>
    <p>Lanternhill delivers directly where you want it within our coverage area.This service is available during restaurant hours</p>
    <div class="btn-ghost" style="left:26px;top:140px;width:100px;height:34px">Learn more</div>
  </div>
  <div class="abs card" style="left:623px">
    <h3>CATERING</h3>
    <p>Do you have to organize lunches or dinners, business events or private parties?Lanternhill will recreate a mediterranean atmosphere in your home or wherever you prefer</p>
    <div class="btn-ghost" style="left:26px;top:140px;width:140px;height:34px">Send your request</div>
  </div>
</section>

<section class="reserve">
  <h2 class="abs center wide-title" style="top:18px">Reserve Now</h2>
  <div class="abs center res-line" style="top:80px"><b>Simple bookings:</b> Tables will only be held for 15 minutes past the reservation time. We appreciate your punctuality.</div>
  <div class="abs center res-line" style="top:108px"><b>Group bookings:</b> All tables of 10 or more guests will have a minimum order requirement of $25 per seat. Please call</div>
  <div class="abs center res-line" style="top:136px">to make a group booking.</div>

  <div class="abs field-label" style="left:122px;top:172px">Name</div>
  <div class="abs field" style="left:122px;top:188px;width:184px"></div>
  <div class="abs field-label" style="left:326px;top:172px">E-mail</div>
  <div class="abs field" style="left:326px;top:188px;width:178px"></div>
  <div class="abs field-label" style="left:530px;top:172px">Date</div>
  <div class="abs field" style="left:530px;top:188px;width:178px"></div>
  <div class="abs field-label" style="left:728px;top:172px">Time</div>
  <div class="abs field" style="left:728px;top:188px;width:181px;font-size:11px;padding:10px;color:#666">--:--</div>
  <div class="abs field-label" style="left:932px;top:172px">People</div>
  <div class="abs field" style="left:932px;top:188px;width:140px;font-size:11px;padding:10px;color:#333">1</div>
  <svg class="abs" style="left:1052px;top:203px" width="10" height="6" viewBox="0 0 10 6"><path d="M0 0l5 6 5-6z" fill="#333"/></svg>

  <div class="btn-red" style="left:510px;top:297px;width:180px;height:42px">Make reservation</div>
</section>

<footer class="footer">
  <div class="abs brand" style="left:122px;top:55px">LANTERNHILL</div>
  <div class="abs foot-text" style="left:122px;top:120px;width:260px">
    <b>Address:</b><br>41 Harbor Row Ste 300<br>Millbrook<br>60911-0420<br><b>Telephone:</b> +1 800 555 0187<br><b>E-mail:</b> hello@lanternhill.example
  </div>
  <div class="abs" style="left:122px;top:250px;display:flex;gap:10px;align-items:center">
    <svg width="10" height="13" viewBox="0 0 10 13"><path d="M5 0a5 5 0 0 1 5 5c0 4-5 8-5 8S0 9 0 5a5 5 0 0 1 5-5z" fill="#fff"/><circle cx="5" cy="5" r="1.8" fill="#000"/></svg>
    <svg width="12" height="12" viewBox="0 0 12 12"><path d="M2 1l2.5 0 1 3-1.5 1a7 7 0 0 0 3 3l1-1.5 3 1V11C6 11 1 6 1 2z" fill="#fff"/></svg>
    <svg width="12" height="12" viewBox="0 0 12 12"><circle cx="6" cy="6" r="6" fill="#fff"/></svg>
    <svg width="12" height="12" viewBox="0 0 12 12"><circle cx="6" cy="6" r="6" fill="#fff"/></svg>
  </div>

  <h3 class="abs foot-head" style="left:437px;top:60px">Opening Hours</h3>
  <div class="abs foot-text" style="left:437px;top:112px">
    <b>Daily from</b> 8am – 10pm<br><b>Friday</b> Closed from Noon – 2pm<br><span style="color:var(--red);font-weight:700">Make a reservation</span>
  </div>

  <h3 class="abs foot-head" style="left:757px;top:60px">Contact Us</h3>
  <div class="abs foot-input" style="top:100px;height:34px">Name</div>
  <div class="abs foot-input" style="top:142px;height:34px">Your email</div>
  <div class="abs foot-input" style="top:184px;height:70px">Message</div>
  <div class="btn-red" style="left:960px;top:265px;width:83px;height:24px;font-size:10px">Submit</div>

  <div class="abs center copy" style="top:296px">Lanternhill Pizza &amp; Wraps © 2017 . Privacy Policy</div>
</footer>

</body>
</html>
```